Specialised investor in e-mobility and energy wants business card design

We need a business card design that fits our existing corporate design. <The look and feel must be 'sharp'/'clean', dynamic, communicate momentum, professionalism etc (as one would imagine from a firm in the financial sector). We like the idea of a reverse-side of the card that includes the logo, and the name and contact details on the other. We expect the deliverable to be whatever format might be required to be able to get cards printed directly by a service such as marlo cards. Our website is www.obrel.finance

```html
<!DOCTYPE html>
<html lang="en">
<head>
<meta charset="utf-8">
<title>Obrel Finance – Business Card</title>
<link href="https://fonts.googleapis.com/css2?family=Montserrat:wght@400;500;700;800&display=swap" rel="stylesheet">
<style>
  :root {
    --stage: #2b2d31;
    --card-white: #ffffff;
    --card-dark: #18181b;
    --green-dark: #24521c;
    --green-light: #6fb23a;
    --text-grey: #5f6368;
    --text-light: #f4f4f4;
  }
  * { box-sizing: border-box; margin: 0; padding: 0; }
  html, body {
    width: 1200px; height: 952px; overflow: hidden;
    background: var(--stage);
    font-family: "Montserrat", sans-serif;
  }
  .stage {
    position: relative; width: 1200px; height: 952px;
    display: flex; align-items: center; justify-content: center; gap: 40px;
  }
  .card {
    position: relative; width: 540px; height: 309px;
    box-shadow: 0 14px 34px rgba(0,0,0,.45);
    overflow: hidden;
  }
  /* Reverse side */
  .card-back { background: var(--card-dark); }
  .card-back .texture {
    position: absolute; inset: 0;
    background: linear-gradient(135deg, #1d1d21 0%, #141417 100%);
  }
  .card-back .brand-mark {
    position: absolute; left: 50%; top: 50%; transform: translate(-50%, -50%);
    display: flex; align-items: center; gap: 10px;
    font-weight: 800; font-size: 40px; letter-spacing: 4px; color: var(--text-light);
  }
  .brand-mark .dot { width: 12px; height: 12px; background: var(--green-light); }

  /* Front side */
  .card-front { background: var(--card-white); }
  .front-brand {
    position: absolute; left: 34px; top: 28px;
    font-weight: 700; font-size: 30px; color: var(--green-dark); letter-spacing: 1px;
  }
  .front-brand span { font-weight: 400; color: var(--green-dark); }
  .contact-list {
    position: absolute; left: 34px; top: 100px; list-style: none;
    display: flex; flex-direction: column; gap: 6px;
  }
  .contact-list li {
    display: flex; align-items: center; gap: 10px;
    font-size: 11.5px; color: var(--text-grey);
  }
  .contact-list .icon {
    width: 16px; height: 16px; background: var(--green-light); border-radius: 2px;
    display: flex; align-items: center; justify-content: center;
  }
  .rule-line {
    position: absolute; left: 0; top: 212px; width: 300px; height: 1.5px;
    background: var(--green-light);
  }
  .holder {
    position: absolute; right: 40px; top: 118px; text-align: right;
  }
  .holder .name {
    font-weight: 800; font-size: 19px; color: var(--green-dark); letter-spacing: .5px;
  }
  .holder .role {
    font-size: 11px; color: var(--text-grey); margin-top: 2px;
    padding-bottom: 5px; border-bottom: 1.5px solid var(--green-light);
    display: inline-block; padding-left: 40px;
  }
  .corner-brand {
    position: absolute; right: 0; bottom: 30px;
    display: flex; align-items: center; gap: 12px;
  }
  .corner-brand .bar { height: 6px; background: var(--green-dark); }
  .corner-brand .bar.left { width: 40px; }
  .corner-brand .bar.right { width: 28px; }
  .corner-brand .word {
    font-weight: 800; font-size: 44px; letter-spacing: 3px; color: var(--green-dark);
  }
</style>
</head>
<body>
<main class="stage">
  <section class="card card-back" aria-label="Card reverse side">
    <div class="texture" role="img" aria-label="Dark background with a faint repeating brand pattern"></div>
    <div class="brand-mark"><span class="dot"></span>OBREL</div>
  </section>

  <section class="card card-front" aria-label="Card front side">
    <div class="front-brand">OBREL <span>Finance</span></div>

    <ul class="contact-list">
      <li><span class="icon"><svg width="10" height="10" viewBox="0 0 10 10"><path d="M2 1l2 2-1 1.2c.6 1.2 1.5 2.1 2.8 2.8L7 6l2 2-1.2 1.2C4.5 9 1 5.5.8 2.2z" fill="#fff"/></svg></span>+41 79555 0148</li>
      <li><span class="icon"><svg width="10" height="10" viewBox="0 0 10 10"><rect x="1" y="2.5" width="8" height="5.5" fill="none" stroke="#fff" stroke-width="1"/><path d="M1 2.5l4 3 4-3" fill="none" stroke="#fff" stroke-width="1"/></svg></span>lena@obrel.finance</li>
      <li><span class="icon"><svg width="10" height="10" viewBox="0 0 10 10"><path d="M5 9.5S1.8 6 1.8 4a3.2 3.2 0 016.4 0C8.2 6 5 9.5 5 9.5z" fill="#fff"/><circle cx="5" cy="4" r="1.2" fill="#6fb23a"/></svg></span>Lugano, Switzerland</li>
      <li><span class="icon"><svg width="10" height="10" viewBox="0 0 10 10"><path d="M2 8l6-6M4 2h4v4" fill="none" stroke="#fff" stroke-width="1.3"/></svg></span>www.obrel.finance</li>
    </ul>

    <div class="rule-line"></div>

    <div class="holder">
      <div class="name">LENA VARGA</div>
      <div class="role">Manager</div>
    </div>

    <div class="corner-brand">
      <span class="bar left"></span>
      <span class="word">OBREL</span>
      <span class="bar right"></span>
    </div>
  </section>
</main>
</body>
</html>
```